Reverse Mortgage Postcard Design - SIZE: 8.5" x 6"

FRONT OF CARD:

HEADLINE:
Reverse Mortgage Program
FHA/ HUD Insured Loan Eliminates Mortgage Payments Forever

You’ve worked hard for your retirement years. You owe it to yourself to find out what the FHA/ HUD Insured Home Equity Conversion Mortgage can do for you. Thousands of Homeowners Nationwide are taking advantage of this program.

If you are 62+ years of age, and live in your own home, you may qualify for this program that allows you to remain in your home while eliminate mortgage payments - FOREVER.

Call Marisol Trent Today for your FREE Information Kit and Private Concierge Consultation
(415) 730-4461

Discover in 2 minutes if a Home Equity Conversion Mortgage is right for you.

INCLUDE IN FRONT OF CARD: COMPANY LOGO & PICTURE OF SENIOR COUPLE

BACK OF CARD - INCLUDE: BRIGHTWAY HOME LOANS LOGO, HEADSHOT OF MARISOL TRENT, FHA LOGO, HUD LOGO, office address:

(BRIGHTWAY HOME LOAN LOGO +)
2715 Orchard Vale Road Suite 300
San Rafael, CA 94817
(415) 730-4461

TESTIMONIAL:

“We had questions if a Reverse Mortgage was right for us. Marisol from Brightway Home Loans was friendly and helped us every step of the way. We couldn’t be happier.” – R. Halvorsen

Benefits Available:
:
 Equity Cash Withdrawal
 Eliminate Mortgage Payments Forever
 Retain Homeownership
 FHA/HUD Insured program

HEADSHOT OF MARISOL TRENT +

Call Marisol Trent
Senior Mortgage Advisor
(415) 730-4461
NMLS # 587430 CA BRE # 2049361

- For Your FREE Information Kit -

FINE PRINT DISCLOSURES (smaller type):

Brightway Home Loans, dba Curtis Bellamy NMLS #615284. 18657 Silver Birch, Dana Point CA 92714. Homeowner remains responsible for paying property taxes, insurance and home maintenance. These materials are not from or approved by HUD.

* ADD FHA AND HUD LOGO *
** Please leave room for mailing indicia and required address space for Post Office **

Target Market(s)

Senior citizens 62+.

Industry/Entity Type

Loan

Requirements
Must have
• I am asking them to trust me with reviewing their finances in relation to their home. It's a very serious proposition, and there are many concerns about security of their financial future..the main thing is, I need to make them pick up the phone and call me. Once I engage with these customers I can gain rapport and provide them excellent service. So if you have any ideas - copy wise - as to how to get them to pick up the phone and call, by all means let me know!!

```html
<!DOCTYPE html>
<html lang="en">
<head>
<meta charset="utf-8">
<title>Reverse Mortgage Postcard</title>
<link rel="stylesheet" href="https://fonts.googleapis.com/css2?family=Lato:ital,wght@0,400;0,700;0,900;1,700;1,900&display=swap">
<style>
  :root {
    --navy: #123a8c;
    --royal: #1f55c8;
    --sky: #3fa3e6;
    --pale-sky: #bfe0f6;
    --ink: #2b2f38;
    --muted: #6b7280;
    --paper: #ffffff;
    --backdrop: #e9ebee;
    --photo-warm: #d9c3a8;
    --photo-cool: #aebfd3;
  }
  * { box-sizing: border-box; margin: 0; padding: 0; }
  html, body { width: 900px; height: 1200px; overflow: hidden; }
  body {
    background: var(--backdrop);
    font-family: "Lato", Arial, sans-serif;
    color: var(--ink);
    position: relative;
  }
  .postcard {
    position: absolute;
    left: 60px;
    width: 780px;
    height: 550px;
    background: var(--paper);
    overflow: hidden;
    box-shadow: 0 4px 14px rgba(0,0,0,.18);
  }
  .postcard--front { top: 30px; }
  .postcard--back { top: 620px; }
  .card-shapes { position: absolute; inset: 0; width: 100%; height: 100%; }
  .abs { position: absolute; }

  /* Front */
  .senior-photo { position: absolute; left: 0; top: 0; width: 440px; height: 330px;
    clip-path: polygon(0 0, 100% 0, 86% 100%, 0 100%);
    background: linear-gradient(135deg, var(--photo-cool), var(--photo-warm) 60%, #c9a98a); }
  .program-title { right: 22px; top: 28px; width: 320px; text-align: right; }
  .program-title h1 { font-weight: 900; font-style: italic; font-size: 21px; color: var(--navy); letter-spacing: .2px; line-height: 1.1; white-space: nowrap; }
  .program-title .sub { font-weight: 700; font-size: 11.5px; color: var(--ink); letter-spacing: .8px; margin-top: 5px; white-space: nowrap; }
  .program-title .forever { font-weight: 400; font-size: 17px; color: var(--sky); letter-spacing: .8px; margin-top: 2px; white-space: nowrap; }
  .about { right: 22px; top: 132px; width: 290px; text-align: right; }
  .about h2 { font-weight: 900; font-size: 16px; color: var(--navy); margin-bottom: 6px; }
  .about p { font-size: 9.5px; line-height: 1.42; color: var(--ink); margin-bottom: 6px; }
  .discover { left: 300px; top: 352px; width: 460px; color: #fff; font-weight: 900; font-size: 20px; line-height: 1.2; }
  .call-today { left: 400px; top: 428px; width: 360px; color: var(--royal); font-weight: 700; font-size: 13px; line-height: 1.35; }
  .free-info { left: 22px; top: 470px; color: #fff; }
  .free-info .label { font-weight: 700; font-size: 15px; }
  .free-info .phone { font-weight: 900; font-size: 24px; }
  .brand-front { left: 22px; top: 18px; color: #fff; font-weight: 900; font-size: 14px; letter-spacing: 1px; display: flex; align-items: center; gap: 6px; }
  .brand-front .dot { width: 12px; height: 12px; border-radius: 50%; background: #fff; }

  /* Back */
  .back-col { left: 40px; top: 44px; width: 420px; }
  .section-head { font-weight: 900; font-size: 16px; letter-spacing: .5px; }
  .section-head--sky { color: var(--sky); }
  .section-head--navy { color: var(--navy); }
  .benefits { list-style: none; display: grid; grid-template-columns: 1fr 1fr; gap: 4px 18px; margin: 8px 0 18px; font-size: 11px; }
  .benefits li { padding-left: 12px; position: relative; }
  .benefits li::before { content: ""; position: absolute; left: 0; top: 5px; width: 5px; height: 5px; border-radius: 50%; background: var(--sky); }
  .advisor { font-size: 11px; line-height: 1.45; margin: 8px 0 16px; }
  .advisor strong { font-weight: 700; }
  .disclosure { font-size: 9px; line-height: 1.45; color: var(--muted); margin-top: 6px; }
  .agency-marks { left: 440px; top: 388px; display: flex; gap: 12px; align-items: center; }
  .agency-badge { width: 46px; height: 32px; background: var(--navy); border-radius: 3px; }
  .agency-badge--round { width: 34px; height: 34px; border-radius: 50%; background: var(--royal); }
  .brand-back { color: var(--navy); font-weight: 900; font-size: 13px; letter-spacing: .5px; display: flex; align-items: center; gap: 6px; white-space: nowrap; }
  .brand-back .dot { width: 12px; height: 12px; background: var(--sky); }
  .office { left: 28px; top: 478px; color: #fff; font-size: 12px; line-height: 1.35; }
  .office .phone { font-weight: 900; font-size: 20px; }
  .mailing-area { left: 520px; top: 190px; width: 220px; }
  .mailing-line { height: 1px; background: #c7ccd4; margin-bottom: 26px; }
  .indicia { right: 34px; top: 34px; width: 74px; height: 56px; border: 1px solid #c7ccd4; }
</style>
</head>
<body>

<section class="postcard postcard--front" aria-label="Postcard front">
  <div class="senior-photo" role="img" aria-label="Photo of a smiling senior couple with family at home"></div>
  <svg class="card-shapes" viewBox="0 0 780 550" aria-hidden="true">
    <polygon points="378,0 404,0 360,330 334,330" fill="#3fa3e6"/>
    <polygon points="410,0 446,0 402,330 366,330" fill="#1f55c8"/>
    <polygon points="0,330 780,330 780,345 0,345" fill="#bfe0f6"/>
    <polygon points="270,340 780,332 780,412 250,412" fill="#1f55c8"/>
    <polygon points="250,412 780,412 780,418 248,418" fill="#3fa3e6"/>
    <polygon points="0,455 360,455 330,550 0,550" fill="#123a8c"/>
    <polygon points="360,455 378,455 348,550 330,550" fill="#3fa3e6"/>
    <polygon points="780,480 780,550 690,550" fill="#3fa3e6"/>
    <polygon points="780,510 780,550 730,550" fill="#123a8c"/>
  </svg>

  <div class="abs brand-front"><span class="dot"></span>BRIGHTWAY HOME LOANS</div>

  <header class="abs program-title">
    <h1>REVERSE MORTGAGE PROGRAM</h1>
    <p class="sub">FHA/ HUD INSURED LOAN ELIMINATES</p>
    <p class="forever">MORTGAGE PAYMENTS FOREVER</p>
  </header>

  <div class="abs about">
    <h2>ABOUT US</h2>
    <p>You’ve worked hard for your retirement years. You owe it to yourself to find out what the FHA/ HUD Insured Home Equity Conversion Mortgage can do for you. Thousands of Homeowners Nationwide are taking advantage of this program.</p>
    <p>If you are 62+ years of age, and live in your own home, you may qualify for this program that allows you to remain in your home while eliminate mortgage payments - FOREVER.</p>
  </div>

  <p class="abs discover">Discover in 2 minutes if a Home Equity Conversion Mortgage is right for you.</p>
  <p class="abs call-today">Call Marisol Trent Today for your free Information Kit and Private Concierge Consultation</p>

  <div class="abs free-info">
    <p class="label">For Free Information</p>
    <p class="phone">(415) 730-4461</p>
  </div>
</section>

<section class="postcard postcard--back" aria-label="Postcard back">
  <svg class="card-shapes" viewBox="0 0 780 550" aria-hidden="true">
    <polygon points="0,0 60,0 0,40" fill="#3fa3e6"/>
    <polygon points="0,0 30,0 0,20" fill="#123a8c"/>
    <polygon points="0,465 300,465 272,550 0,550" fill="#123a8c"/>
    <polygon points="300,465 316,465 288,550 272,550" fill="#3fa3e6"/>
    <polygon points="780,500 780,550 700,550" fill="#3fa3e6"/>
  </svg>

  <div class="abs back-col">
    <h2 class="section-head section-head--sky">BENEFITS AVAILABLE</h2>
    <ul class="benefits">
      <li>Equity Cash Withdrawal</li>
      <li>Retain Homeownership</li>
      <li>Eliminate Mortgage Payments Forever</li>
      <li>FHA/HUD Insured program</li>
    </ul>
    <h2 class="section-head section-head--navy">HEADSHOT OF MARISOL TRENT</h2>
    <p class="advisor"><strong>Call Marisol Trent</strong><br>Senior Mortgage Advisor<br>(415) 730-4461<br>NMLS # 587430 CA BRE # 2049361</p>
    <h2 class="section-head section-head--sky">DISCLOSURES</h2>
    <p class="disclosure">Brightway Home Loans, dba Curtis Bellamy NMLS #615284. 18657 Silver Birch, Dana Point CA 92714. Homeowner remains responsible for paying property taxes, insurance and home maintenance. These materials are not from or approved by HUD.</p>
  </div>

  <div class="abs indicia"></div>
  <div class="abs mailing-area">
    <div class="mailing-line"></div>
    <div class="mailing-line"></div>
    <div class="mailing-line"></div>
    <div class="mailing-line"></div>
  </div>

  <div class="abs agency-marks">
    <span class="agency-badge"></span>
    <span class="agency-badge agency-badge--round"></span>
    <span class="brand-back"><span class="dot"></span>BRIGHTWAY HOME LOANS</span>
  </div>

  <div class="abs office">
    <p>2715 Orchard Vale Road Suite 300</p>
    <p>San Rafael, CA 94817</p>
    <p class="phone">(415) 730-4461</p>
  </div>
</section>

</body>
</html>
```